Stationery for London Estate Agents (Real Estate)

We are a modern and professional Estate Agency (Realtors) working with high quality properties in London.
We wish to redesign our stationary using our branding displayed on the front of our offices and require a digital version of this logo to be produced (photograph attached). Slight 'tweaking' of this branding is acceptable.
Updates
1st July 2010 Thank you all those designers who have uploaded submissions. Business Card - Details Side: Business Card - Logo Side: Outline of London Skyline Examples of the london skyline are available at http://www.pixorabank.example/searchkwy_london-skyline-silhouette Please be advised that we are looking for an outline, not a 'filled in' silhouette. Letterhead Please feel free to ask us any questions. Bertrand
I have been able to further refine our design requirements based on your submissions.
We like Blue Kettle' business card submission that has not been eliminated and have the following design clarifications;
a) Please use an email icon (e.g an envelope).
b) Please make the email as equally prominent as the telephone and fax
c) We very much like Fernwicky's 'mini window icon' - please display the website URL under such a mini window icon at the bottom right of the card.
We are very happy with the colouring, fonts and proportions used by Blue Kettle.
We invite designers to try adding an outline of the London Skyline to the left of the large window icon on the business card and in a suitablie position on the Letterhead (e.g at the top left of the letterhead).
We have the following design clarifiications to our Letterhead requirements;
A) We would like the main logo to be on the top right side of the letterhead.
B) We do NOT want the large window icon to be on the left of the logo or the bottom of the letterhead. We are happy having the large window icon to the right or underneath the TK brand.
C) Please use icons for tel, fax and email (e.g. envelope icon for e-mail address)
D) We like two coloured red borders, one at the top and bottom of the letterhead but are happy for variations in shape and size.
E) We currently prefer our address and contact details at the bottom of the letterhead.
F) We like Fernwicky's 'mini window icon' and would prefer this to be used to display the website URL at the bottom right of the letterhead.
G) Please be advised that the letterhead does NOT need additional space for the Company Name as per Blue Kettle' submission - the TK brand is sufficient.
Target Market(s)
Owners of high quality property in London.
Industry/Entity Type
Real Estate
Requirements
Must have
- Business Cards: We would like a 'vertical' style business card with our branding on one side and our staff's details on the other;
- Our website is www.tolkane.example and we are flexible where that should be on the card and letterhead.
- Stationery details are available in a file attached to this project.
Nice to have
- It would be great to have a horizontal version of the digital logo for placement on property portals (150x60)
Should not have
- Logo should not deviate significantly from the branding on our offices (shop front) - photograph attached.

```html
<!DOCTYPE html>
<html lang="en">
<head>
<meta charset="utf-8">
<title>Tolkane Residential – Stationery</title>
<link rel="stylesheet" href="https://fonts.googleapis.com/css2?family=Arimo:wght@400;700&display=swap">
<style>
  :root {
    --magenta: #c11d72;
    --yellow: #f7e13d;
    --ink: #111111;
    --paper: #ffffff;
    --canvas: #ffffff;
    --shadow: 6px 6px 5px rgba(0, 0, 0, 0.45);
  }
  * { box-sizing: border-box; margin: 0; padding: 0; }
  html, body { width: 1200px; height: 900px; overflow: hidden; background: var(--canvas); }
  body { position: relative; font-family: "Arimo", Arial, sans-serif; color: var(--ink); }

  .sheet { position: absolute; background: var(--paper); box-shadow: var(--shadow); overflow: hidden; }
  .brand-mark { display: inline-block; width: 14px; height: 14px; background: var(--yellow); }

  /* Letterhead */
  .letterhead { left: 415px; top: 22px; width: 597px; height: 845px; }
  .letterhead__strip { position: absolute; top: 0; right: 0; width: 127px; height: 100%; background: var(--magenta); }
  .letterhead__brand { position: absolute; right: 137px; top: 6px; color: var(--magenta); line-height: 1; text-align: right; white-space: nowrap; }
  .letterhead__brand-name { display: block; font-size: 50px; }
  .letterhead__brand-name .brand-mark { margin-right: 12px; vertical-align: 8px; }
  .letterhead__brand-sub { display: block; font-size: 42px; margin-right: 10px; margin-top: 2px; }
  .letterhead__tagline { position: absolute; left: 232px; top: 109px; font-size: 13px; color: var(--magenta); word-spacing: 3px; white-space: nowrap; }
  .letterhead__contact { position: absolute; right: 14px; top: 122px; text-align: right; color: var(--paper); font-size: 11px; line-height: 13px; white-space: nowrap; }
  .letterhead__contact p + p { margin-top: 12px; }
  .accent { color: var(--yellow); }
  .letterhead__legal { position: absolute; right: 138px; bottom: 44px; text-align: right; font-size: 9.5px; line-height: 12px; white-space: nowrap; }

  /* Business card, logo side */
  .card-front { left: 282px; top: 190px; width: 153px; height: 240px; background: var(--magenta); color: var(--paper); }
  .card-front__brand { position: absolute; left: 14px; top: 72px; line-height: 1; white-space: nowrap; }
  .card-front__brand-name { display: block; font-size: 21px; }
  .card-front__brand-sub { display: block; font-size: 18px; margin-left: 10px; margin-top: 1px; }
  .card-front__tagline { position: absolute; left: 24px; top: 117px; font-size: 6.5px; word-spacing: 2px; white-space: nowrap; }
  .card-front__url { position: absolute; left: 14px; bottom: 8px; font-size: 8.5px; }

  /* Business card, details side */
  .card-back { left: 455px; top: 190px; width: 151px; height: 240px; }
  .card-back__strip { position: absolute; top: 0; right: 0; width: 24px; height: 100%; background: var(--magenta); }
  .card-back__details { position: absolute; right: 30px; top: 8px; text-align: right; font-size: 10px; line-height: 12.5px; white-space: nowrap; }
  .card-back__brand { color: var(--magenta); font-size: 18px; line-height: 1; }
  .card-back__brand span { display: block; }
  .card-back__name { color: var(--magenta); font-size: 11.5px; margin-top: 14px; }
  .card-back__details .group { margin-top: 13px; }

  /* Invitation */
  .invitation { left: 147px; top: 465px; width: 594px; height: 285px; }
  .invitation__art { position: absolute; inset: 0; }
  .invitation__body { position: absolute; left: 14px; top: 12px; font-size: 17.5px; line-height: 21px; white-space: nowrap; }
  .invitation__body p { margin-bottom: 18px; }
  .invitation__brand { position: absolute; left: 350px; top: 10px; color: var(--paper); line-height: 1; white-space: nowrap; }
  .invitation__brand-name { display: block; font-size: 38px; }
  .invitation__brand-sub { display: block; font-size: 32px; margin-left: 16px; margin-top: 2px; }
  .invitation__brand-sub .brand-mark { margin-left: 12px; vertical-align: 2px; }
</style>
</head>
<body>

<section class="sheet letterhead" aria-label="Letterhead">
  <div class="letterhead__strip"></div>
  <div class="letterhead__brand">
    <span class="letterhead__brand-name"><span class="brand-mark"></span>TOLKANE</span>
    <span class="letterhead__brand-sub">residential</span>
  </div>
  <p class="letterhead__tagline">Sales - Lettings - Management</p>
  <div class="letterhead__contact">
    <p>020 7946 0400 <span class="accent">T</span><br>020 7946 0522 <span class="accent">F</span></p>
    <p>bertrand<span class="accent">@</span>tolkane.uk<br>info<span class="accent">@</span>tolkane.uk</p>
    <p>48 Larkmoor Road<br>Hampstead<br>London<br>NW3 9QX<br><span class="accent">www.tolkane.example</span></p>
  </div>
  <p class="letterhead__legal">Tolkane Residential is a trade name for Harbrook Estates Limited registered in England and Wales<br>Company Registration No. 07381264</p>
</section>

<section class="sheet card-front" aria-label="Business card, logo side">
  <div class="card-front__brand">
    <span class="card-front__brand-name">TOLKANE</span>
    <span class="card-front__brand-sub">residential</span>
  </div>
  <p class="card-front__tagline">Sales - Lettings - Management</p>
  <p class="card-front__url">www.tolkane.example</p>
</section>

<section class="sheet card-back" aria-label="Business card, details side">
  <div class="card-back__strip"></div>
  <div class="card-back__details">
    <p class="card-back__brand"><span>TOLKANE</span><span>residential</span></p>
    <p class="card-back__name">BERTRAND LOWELL</p>
    <p class="group">07700 900 415 M<br>020 7946 0400 T<br>020 7946 0522 F</p>
    <p class="group">bertrand@tolkane.uk</p>
    <p class="group">48 Larkmoor Road<br>Hampstead<br>London<br>NW3 9QX</p>
  </div>
</section>

<section class="sheet invitation" aria-label="Open House invitation">
  <svg class="invitation__art" width="594" height="285" viewBox="0 0 594 285" aria-hidden="true">
    <polygon points="305,0 594,0 594,285 483,285" fill="var(--magenta)"/>
    <text x="0" y="0" transform="translate(258,12) rotate(58)" font-family="Arimo, Arial, sans-serif" font-size="48" fill="var(--magenta)" textLength="318" lengthAdjust="spacingAndGlyphs">INVITATION</text>
  </svg>
  <div class="invitation__body">
    <p>Dear</p>
    <p>Please accept our invitation to our<br>Open House Day.&nbsp; Your attendance<br>will be gladly welcomed...</p>
    <p>Date:</p>
    <p>Address:</p>
    <p>RSVP:</p>
    <p>Refreshments will be available.</p>
  </div>
  <div class="invitation__brand">
    <span class="invitation__brand-name">TOLKANE</span>
    <span class="invitation__brand-sub">residential<span class="brand-mark"></span></span>
  </div>
</section>

</body>
</html>
```